Mr. Kelpie Restaurant Menu Design

I would like for you to please create a menu design for my seafood restaurant called Mr. Kelpie. I uploaded the logo of my restaurant and would like the same colors and font to be used on the menu. The headings of my menu should include the following:
What's your catch?
What's your sauce?
How "Hot" can you go?
Medium?
Mild?
Wild?
Soups
Paella
Katsu
Add Ons
Sweet Cravings
Thirsty?
It would be nice to see something creative and simple preferably one page.
I already uploaded my logo on the brief section.
Thank you.
Target Market(s)
Family friendly
Industry/Entity Type
Seafood Restaurant
Look and feel

```html
<!DOCTYPE html>
<html lang="en">
<head>
<meta charset="utf-8">
<title>Mr. Kelpie Restaurant Menu</title>
<link href="https://fonts.googleapis.com/css2?family=Titan+One&family=Varela+Round&family=Open+Sans:wght@400;600&display=swap" rel="stylesheet">
<style>
  :root{
    --orange:#f28a1f;
    --orange-deep:#e4731a;
    --blue:#1e9be0;
    --navy:#0d3a6b;
    --item-blue:#1a3e8c;
    --ink:#222;
    --white:#ffffff;
    --panel:rgba(255,255,255,0.82);
  }
  *{margin:0;padding:0;box-sizing:border-box}
  html,body{width:848px;height:1200px;overflow:hidden;background:var(--orange)}
  .menu{position:relative;width:848px;height:1200px;overflow:hidden;background:var(--orange);font-family:"Open Sans",Arial,sans-serif}
  .header-art{position:absolute;left:0;top:0}
  .seascape{position:absolute;left:0;top:400px;width:848px;height:660px;
    background:linear-gradient(180deg,#9fd3ef 0%,#5fb5de 30%,#2f8fc4 55%,#e8b48c 75%,#e7864a 100%)}
  .panel{position:absolute;left:40px;top:406px;width:769px;height:646px;background:var(--panel)}
  .brand-mark{position:absolute;left:333px;top:32px;width:182px;height:182px;border-radius:50%;background:var(--blue);border:5px solid var(--white)}
  .brand-name{position:absolute;left:0;top:208px;width:848px;text-align:center;font-family:"Titan One",sans-serif;font-size:56px;color:var(--white);line-height:1}
  .taglines{position:absolute;left:0;top:316px;width:848px;text-align:center;font-family:"Titan One",sans-serif;font-size:18px;color:var(--white);word-spacing:2px;
    -webkit-text-stroke:3px var(--navy);paint-order:stroke fill;letter-spacing:.3px}
  .heat{position:absolute;left:0;top:344px;width:848px;text-align:center;font-family:"Titan One",sans-serif;font-size:44px;color:var(--blue);word-spacing:14px;
    -webkit-text-stroke:5px var(--navy);paint-order:stroke fill}
  .section-title{position:absolute;font-family:"Titan One",sans-serif;font-size:29px;color:var(--orange);line-height:1;
    -webkit-text-stroke:6px var(--white);paint-order:stroke fill;filter:drop-shadow(0 0 1px #6b3000) drop-shadow(0 0 1px #6b3000)}
  .item{position:absolute;width:310px}
  .item-name{font-family:"Varela Round",sans-serif;font-size:16px;color:var(--item-blue);line-height:20px}
  .item-desc{font-size:12px;color:var(--ink);line-height:14px;width:310px}
  .item-price{position:absolute;top:-2px;font-family:"Varela Round",sans-serif;font-size:18px;color:var(--item-blue)}
  .col-left .item{left:81px}
  .col-left .item-price{left:246px}
  .col-right .item{left:440px;width:345px}
  .col-right .item-desc{width:330px}
  .col-right .item-price{left:248px}
  .col-right .sweet .item-desc{width:245px}
  .col-right .drink .item-desc{width:235px;padding-top:2px}
  .footer-art{position:absolute;left:0;top:1040px}
  .contact{position:absolute;left:80px;display:flex;align-items:center;gap:12px;font-family:"Varela Round",sans-serif;font-weight:600;font-size:17px;color:var(--white)}
  .contact svg{flex:none}
  .social{position:absolute;left:383px;top:1132px;display:flex;align-items:center;gap:14px;font-family:"Varela Round",sans-serif;font-size:17px;color:var(--white)}
  .social-label{margin-right:6px;font-weight:600}
  .social-tile{width:36px;height:36px;border-radius:3px;background:var(--blue);border:2px solid var(--white)}
</style>
</head>
<body>
<main class="menu">

  <svg class="header-art" width="848" height="410" viewBox="0 0 848 410">
    <rect width="848" height="410" fill="var(--orange)"/>
    <g role="img" aria-label="Blue sky with soft white clouds">
      <defs>
        <linearGradient id="sky" x1="0" y1="0" x2="0" y2="1">
          <stop offset="0" stop-color="#2e8fd6"/>
          <stop offset="0.6" stop-color="#4ea7e3"/>
          <stop offset="1" stop-color="#7cc0ec"/>
        </linearGradient>
      </defs>
      <path d="M0 110 Q424 40 848 92 L848 280 Q424 262 0 290 Z" fill="url(#sky)"/>
    </g>
    <path d="M0 62 Q424 -6 848 52" fill="none" stroke="var(--white)" stroke-width="8"/>
    <path d="M0 90 Q424 22 848 76" fill="none" stroke="var(--white)" stroke-width="6"/>
    <path d="M0 118 Q424 50 848 102" fill="none" stroke="var(--orange)" stroke-width="10"/>
    <path d="M0 290 Q424 262 848 280" fill="none" stroke="var(--white)" stroke-width="6"/>
  </svg>

  <div class="seascape" role="img" aria-label="Tropical bay with cliffs and a plate of cooked crab"></div>
  <div class="panel"></div>

  <div class="brand-mark"></div>
  <div class="brand-name">Mr. Kelpie</div>

  <p class="taglines">WHAT’S YOUR CATCH? &nbsp;WHAT’S YOUR SAUCE? &nbsp;HOW “HOT CAN YOU GO?</p>
  <p class="heat">Medium? Mild? Wild?</p>

  <section class="col-left">
    <h2 class="section-title" style="left:82px;top:444px">Soups</h2>
    <div class="item" style="top:492px"><div class="item-name">Tuna Carpaccio</div><div class="item-desc">Poached lobster, honey tomato, avocado, tuna tapenade</div><span class="item-price">$30</span></div>
    <div class="item" style="top:558px"><div class="item-name">Cheese soufflé</div><div class="item-desc">Morels crème, arugula salad and hazelnuts</div><span class="item-price">$30</span></div>
    <div class="item" style="top:610px"><div class="item-name">Lobster salad</div><div class="item-desc">Herb and cauliflower salad, lemon cress, citrus dressing</div><span class="item-price">$30</span></div>
    <div class="item" style="top:676px"><div class="item-name">Baked chermoula prawns</div><div class="item-desc">Stuffed with scallops, eggplant romesco, almond and pistachio</div><span class="item-price">$30</span></div>
    <div class="item" style="top:743px"><div class="item-name">Prawn and calamari salad</div><div class="item-desc">Cured salmon, mango, crisp vegetables.</div><span class="item-price">$30</span></div>

    <h2 class="section-title" style="left:82px;top:800px">Katsu</h2>
    <div class="item" style="top:856px"><div class="item-name">King Crab Rillette</div><div class="item-desc">Watermelon, smoked trout, herb salad</div><span class="item-price">$20</span></div>
    <div class="item" style="top:900px"><div class="item-name">Robian Salad</div><div class="item-desc">Arugula, halloumi and pomegranate</div><span class="item-price">$20</span></div>
    <div class="item" style="top:944px"><div class="item-name">Salmon roulade</div><div class="item-desc">Basil tabouleh, marinated daikon, citra leaves</div><span class="item-price">$20</span></div>
    <div class="item" style="top:996px"><div class="item-name">Pan fried Scallops</div><div class="item-desc">Stuffed calamari, squid ink risotto, micro herbs</div><span class="item-price">$20</span></div>
  </section>

  <section class="col-right">
    <h2 class="section-title" style="left:470px;top:440px">Add Ons</h2>
    <div class="item" style="top:495px"><div class="item-name">Robian Salad</div><div class="item-desc">Arugula, halloumi and pomegranate</div><span class="item-price">$10.75</span></div>
    <div class="item" style="top:546px"><div class="item-name">Salmon roulade</div><div class="item-desc">Basil tabouleh, marinated daikon, citra leaves</div><span class="item-price">$9.75</span></div>
    <div class="item" style="top:597px"><div class="item-name">Pan fried Scallops</div><div class="item-desc">Stuffed calamari, squid ink risotto, micro herbs</div><span class="item-price">$8.25</span></div>

    <h2 class="section-title" style="left:468px;top:654px">Sweet Cravings</h2>
    <div class="item sweet" style="top:697px"><div class="item-name">Homemade Tiramisu</div><div class="item-desc">Layers of marscapone cheese and lady fingers soaked in coffee</div><span class="item-price" style="top:12px">$8.25</span></div>
    <div class="item sweet" style="top:763px"><div class="item-name">Jamaica Mud Cake</div><div class="item-desc">Dark chocolate sponge with a middle layer of chocolate ganache</div><span class="item-price" style="top:12px">$8.25</span></div>
    <div class="item sweet" style="top:830px"><div class="item-name">Bianco &amp; Nero</div><div class="item-desc">Profiterole filled with vanilla custard and coverture of milk chocolate</div><span class="item-price">$8.25</span></div>

    <h2 class="section-title" style="left:478px;top:892px">Thirsty?</h2>
    <div class="item drink" style="top:942px"><div class="item-desc">Filter Coffe, decaf coffee, plain hot chocolate</div><span class="item-price" style="top:-2px">$8.25</span></div>
    <div class="item drink" style="top:988px"><div class="item-desc">Assorted premium “Leaf &amp; Kettle” teas</div><span class="item-price" style="top:-2px">$8.25</span></div>
    <div class="item drink" style="top:1016px"><div class="item-desc">Hot chocolate with cream</div><span class="item-price" style="top:-2px">$8.25</span></div>
  </section>

  <svg class="footer-art" width="848" height="160" viewBox="0 0 848 160">
    <path d="M0 14 Q424 4 848 10 L848 160 L0 160 Z" fill="var(--orange)"/>
    <path d="M0 20 Q424 10 848 16" fill="none" stroke="var(--white)" stroke-width="6"/>
    <path d="M0 40 Q424 28 848 36" fill="none" stroke="var(--white)" stroke-width="5"/>
    <path d="M0 58 Q424 46 848 54" fill="none" stroke="var(--orange-deep)" stroke-width="4"/>
  </svg>

  <div class="contact" style="top:1116px">
    <svg width="26" height="26" viewBox="0 0 26 26"><circle cx="13" cy="13" r="13" fill="var(--blue)"/><path d="M6 13.5 L13 7 L20 13.5 M8.5 12 V19 H17.5 V12" fill="none" stroke="var(--white)" stroke-width="2.2" stroke-linejoin="round"/></svg>
    <span>Your Address</span>
  </div>
  <div class="contact" style="top:1150px">
    <svg width="26" height="26" viewBox="0 0 26 26"><circle cx="13" cy="13" r="13" fill="var(--blue)"/><path d="M7 11 Q13 7 19 11 L18 13 L15.5 12.5 L15 11 H11 L10.5 12.5 L8 13 Z M9 14 H17 L18 19 H8 Z" fill="var(--white)"/></svg>
    <span>0123-5523-254</span>
  </div>

  <div class="social">
    <span class="social-label">Find us @Mr. Kelpie on</span>
    <span class="social-tile"></span>
    <span class="social-tile"></span>
    <span class="social-tile"></span>
    <span class="social-tile"></span>
  </div>

</main>
</body>
</html>
```